Velmira Body Oil Label for 4 -8 oz bottles

We are selling 4 and 8 oz body oils and need a label to put on our bottles. I'm not sure if we want a label for the front and also the back of the bottle or just one label in the front. You can give me examples of each way. Attached is our logo on a blue background but the background will change colors depending on the scent as specified in the design description. Our bottle will be either clear or white with a pump spray type lid as shown in the attached example. Attached are also our design criteria which is needed for the labels.
Updates

We have decided to use the disc top cap and not the pump spray cap. If you are able to, please show us the design on the 4 oz bottle with the disc top cap. Thanks

Target Market(s)

women

Industry/Entity Type

skincare, cosmetics

Font styles to use
Serif
Sans Serif

Requirements
Must have
• stylish name for each scented oil which contrasts the font in the logo. Also must have darker colors since the logo colors are lighter.
Nice to have
• Border around the labels, maybe one solid color or maybe two complimenting colors which go well with the fragrnace name
Should not have
• background colors that match the logo colors

```html
<!DOCTYPE html>
<html lang="en">
<head>
<meta charset="utf-8">
<title>Velmira Body Oils – Cotton Candy Label</title>
<link href="https://fonts.googleapis.com/css2?family=Fredoka:wght@600;700&family=Poppins:wght@400;500&display=swap" rel="stylesheet">
<style>
  :root {
    --backdrop: #5ab5c4;
    --sky: #92d6df;
    --candy: #f2aec0;
    --candy-deep: #ef7f9c;
    --aqua-text: #6cc5d3;
    --ink: #2a2a2a;
    --white: #ffffff;
    --warn-red: #e0323a;
  }
  * { box-sizing: border-box; margin: 0; padding: 0; }
  html, body { width: 785px; height: 1200px; overflow: hidden; }
  body {
    background: var(--backdrop);
    font-family: "Poppins", sans-serif;
    color: var(--ink);
    position: relative;
  }
  .label {
    position: absolute;
    left: 42px; top: 425px;
    width: 700px; height: 350px;
    display: flex;
    box-shadow: 0 14px 30px rgba(0,0,0,0.18);
  }
  .panel { position: relative; width: 233.34px; height: 100%; overflow: hidden; }
  .panel-info { background: linear-gradient(180deg, #ffffff 55%, #eef8fa 100%); }
  .panel-front { background: var(--candy); }
  .panel-warnings { background: linear-gradient(160deg, #ffffff 50%, #fdebef 100%); }

  .heading {
    font-family: "Fredoka", sans-serif;
    font-weight: 700;
    font-size: 11px;
    letter-spacing: 0.2px;
    text-transform: uppercase;
  }
  .heading-aqua { color: var(--aqua-text); }
  .heading-pink { color: var(--candy-deep); }
  .copy { font-size: 8.6px; line-height: 12px; color: var(--ink); }

  .sparkle { position: absolute; }

  /* info panel */
  .ingredients { position: absolute; left: 21px; top: 84px; width: 180px; }
  .directions { position: absolute; left: 21px; top: 200px; width: 160px; }
  .ingredients .copy, .directions .copy { margin-top: 8px; }

  /* front panel */
  .sky-band { position: absolute; left: 0; top: 0; width: 100%; height: 140px; background: var(--sky); }
  .brand {
    position: absolute; top: 48px; left: 0; width: 100%;
    display: flex; align-items: center; justify-content: center; gap: 7px;
  }
  .brand-dot { width: 10px; height: 10px; border-radius: 50%; background: var(--white); }
  .brand-name {
    font-family: "Poppins", sans-serif; font-weight: 500;
    font-size: 26px; color: var(--white); letter-spacing: 1px;
  }
  .wave-top { position: absolute; left: 0; top: 124px; width: 100%; height: 20px; }
  .cloud {
    position: absolute; border-radius: 50%;
    background: radial-gradient(ellipse at center, rgba(255,255,255,0.9) 0%, rgba(255,255,255,0.35) 55%, rgba(255,255,255,0) 75%);
  }
  .cloud-left { left: -6px; top: 108px; width: 90px; height: 44px; }
  .cloud-right { left: 170px; top: 212px; width: 80px; height: 40px; }
  .scent-name {
    position: absolute; top: 168px; left: 0; width: 100%;
    text-align: center;
    font-family: "Fredoka", sans-serif; font-weight: 700;
    font-size: 38px; line-height: 36px; color: var(--white);
    letter-spacing: 0.5px;
  }
  .features {
    position: absolute; top: 262px; left: 0; width: 100%;
    display: flex; flex-wrap: wrap; justify-content: center;
    gap: 4px 12px; padding: 0 30px;
    font-family: "Fredoka", sans-serif; font-weight: 600;
    font-size: 9.5px; color: var(--white);
  }
  .feature { display: flex; align-items: center; gap: 4px; white-space: nowrap; }
  .feature svg { width: 11px; height: 11px; }
  .net-weight {
    position: absolute; top: 314px; left: 65px;
    width: 104px; height: 17px; border-radius: 9px;
    background: var(--white);
    font-size: 7.2px; line-height: 17px; text-align: center; color: var(--ink);
  }

  /* warnings panel */
  .warnings { position: absolute; left: 20px; top: 84px; width: 200px; }
  .warnings-title { display: flex; align-items: center; gap: 6px; }
  .alert-dot {
    width: 11px; height: 11px; border-radius: 50%; background: var(--warn-red);
    color: var(--white); font-size: 8px; font-weight: 500; line-height: 11px; text-align: center;
  }
  .warning-list { list-style: none; margin-top: 9px; }
  .warning-list li { display: flex; gap: 9px; font-size: 8.6px; line-height: 11px; margin-bottom: 3.6px; }
  .warning-list .cross { color: var(--warn-red); font-weight: 500; font-size: 10px; width: 8px; flex-shrink: 0; }
  .distributor-band { position: absolute; left: 0; top: 258px; width: 100%; height: 92px; }
  .distributor {
    position: absolute; left: 20px; top: 290px;
    font-size: 9.4px; line-height: 14.5px; color: var(--white); font-weight: 500;
  }
  .origin-badge {
    position: absolute; left: 158px; top: 238px;
    width: 50px; height: 50px; border-radius: 50%;
    background: #c8283a; border: 3px solid var(--white);
    box-shadow: 0 0 0 2px #1f3a8a;
  }
  .corner-dot { position: absolute; left: 205px; top: 312px; width: 12px; height: 12px; border-radius: 50%; background: var(--white); opacity: 0.9; }
</style>
</head>
<body>
  <main class="label">
    <!-- info panel -->
    <section class="panel panel-info">
      <svg class="sparkle" style="left:171px;top:124px" width="16" height="16" viewBox="0 0 16 16"><path d="M8 0 Q9 7 16 8 Q9 9 8 16 Q7 9 0 8 Q7 7 8 0Z" fill="#f2aec0"/></svg>
      <div class="ingredients">
        <h2 class="heading heading-aqua">Ingredients</h2>
        <p class="copy">Cocos Nucifera (Coconut) Oil, Prunus Amygdalus Dulcis (Almond) Oil, Vitis Vinifera (Grapeseed) Oil, Sesamum Indicum (Sesame) Seed Oil, Simmondsia Chinensis (Jojoba) Oil, Tocopheryl Acetate (Vitamin E). Essential oils, and fragrances.</p>
      </div>
      <div class="directions">
        <h2 class="heading heading-aqua">Directions</h2>
        <p class="copy">Apply a small amount to skin and massage until absorbed. Use daily for best results.</p>
      </div>
      <svg class="sparkle" style="left:172px;top:270px" width="9" height="9" viewBox="0 0 16 16"><path d="M8 0 Q9 7 16 8 Q9 9 8 16 Q7 9 0 8 Q7 7 8 0Z" fill="#6cc5d3"/></svg>
      <svg class="sparkle" style="left:43px;top:286px" width="16" height="16" viewBox="0 0 16 16"><path d="M8 0 Q9 7 16 8 Q9 9 8 16 Q7 9 0 8 Q7 7 8 0Z" fill="#6cc5d3"/></svg>
    </section>

    <!-- front panel -->
    <section class="panel panel-front">
      <div class="sky-band"></div>
      <div class="brand">
        <span class="brand-dot"></span>
        <span class="brand-name">Velmira</span>
      </div>
      <svg class="wave-top" viewBox="0 0 234 20" preserveAspectRatio="none">
        <path d="M0 10 Q7 2 14.6 10 T29.2 10 T43.8 10 T58.4 10 T73 10 T87.6 10 T102.2 10 T116.8 10 T131.4 10 T146 10 T160.6 10 T175.2 10 T189.8 10 T204.4 10 T219 10 T234 10 V20 H0Z" fill="#f2aec0" stroke="#ffffff" stroke-width="2.5"/>
      </svg>
      <div class="cloud cloud-left" role="img" aria-label="soft white clouds"></div>
      <div class="cloud cloud-right" role="img" aria-label="soft white clouds"></div>
      <h1 class="scent-name">COTTON<br>CANDY</h1>
      <svg class="sparkle" style="left:200px;top:183px" width="8" height="8" viewBox="0 0 16 16"><path d="M8 0 Q9 7 16 8 Q9 9 8 16 Q7 9 0 8 Q7 7 8 0Z" fill="#fff"/></svg>
      <svg class="sparkle" style="left:36px;top:218px" width="10" height="10" viewBox="0 0 16 16"><path d="M8 0 Q9 7 16 8 Q9 9 8 16 Q7 9 0 8 Q7 7 8 0Z" fill="#fff"/></svg>
      <div class="features">
        <span class="feature"><svg viewBox="0 0 12 12"><circle cx="6" cy="6" r="5" fill="none" stroke="#fff" stroke-width="1.2"/><line x1="2.5" y1="9.5" x2="9.5" y2="2.5" stroke="#fff" stroke-width="1.2"/></svg>Non - Greesy</span>
        <span class="feature"><svg viewBox="0 0 12 12"><path d="M6 1 Q10 6 10 8 A4 4 0 0 1 2 8 Q2 6 6 1Z" fill="#fff"/></svg>With Vitamin E</span>
        <span class="feature"><svg viewBox="0 0 12 12"><path d="M6 1 Q9 5 9 7 A3 3 0 0 1 3 7 Q3 5 6 1Z" fill="#fff"/><path d="M1 10 Q6 12 11 10" stroke="#fff" stroke-width="1" fill="none"/></svg>Ultra Moisturizing</span>
      </div>
      <div class="net-weight">Net Wt. 4 fl. oz. (118 mL)</div>
    </section>

    <!-- warnings panel -->
    <section class="panel panel-warnings">
      <svg class="sparkle" style="left:170px;top:50px" width="18" height="18" viewBox="0 0 16 16"><path d="M8 0 Q9 7 16 8 Q9 9 8 16 Q7 9 0 8 Q7 7 8 0Z" fill="#f2aec0"/></svg>
      <svg class="sparkle" style="left:190px;top:62px" width="9" height="9" viewBox="0 0 16 16"><path d="M8 0 Q9 7 16 8 Q9 9 8 16 Q7 9 0 8 Q7 7 8 0Z" fill="#f2aec0"/></svg>
      <div class="warnings">
        <div class="warnings-title"><span class="alert-dot">!</span><h2 class="heading heading-pink">Warnings / Disclaimers</h2></div>
        <ul class="warning-list">
          <li><span class="cross">✕</span>For external use only.</li>
          <li><span class="cross">✕</span>Avoid contact with eyes.</li>
          <li><span class="cross">✕</span>Discontinue use if irritation occurs.</li>
          <li><span class="cross">✕</span>Keep out of reach of children.</li>
          <li><span class="cross">✕</span>Contains nut oils — use with caution if you have nut allergies.</li>
        </ul>
      </div>
      <svg class="sparkle" style="left:68px;top:222px" width="16" height="16" viewBox="0 0 16 16"><path d="M8 0 Q9 7 16 8 Q9 9 8 16 Q7 9 0 8 Q7 7 8 0Z" fill="#6cc5d3"/></svg>
      <svg class="distributor-band" viewBox="0 0 234 92" preserveAspectRatio="none">
        <path d="M0 10 Q7 2 14.6 10 T29.2 10 T43.8 10 T58.4 10 T73 10 T87.6 10 T102.2 10 T116.8 10 T131.4 10 T146 10 T160.6 10 T175.2 10 T189.8 10 T204.4 10 T219 10 T234 10 V92 H0Z" fill="#92d6df" stroke="#f2aec0" stroke-width="2.5"/>
      </svg>
      <div class="origin-badge" role="img" aria-label="origin badge"></div>
      <p class="distributor">Distributed by Velmira<br>2217 Alder Crest Lane<br>Fort Collins, CO 80525</p>
      <span class="corner-dot"></span>
    </section>
  </main>
</body>
</html>
```